Update existing Product Data Sheets with new design / multi page layout

We are looking to update the design for our products data sheets. Here is a link to our most popular product http://www.corvantel-power.com/products/12v-100ah-lithium-ion-battery/

I am also attaching the current data sheet. Most of the information on the new data sheet will come from what is on our website.

Industry/Entity Type

Product

Requirements
Must have
• Clean, simple and corporate look. multi page design, two or more pages.
Nice to have
• would like to put infographics in place of some content if possible.

```html
<!DOCTYPE html>
<html lang="en">
<head>
<meta charset="utf-8">
<title>Product Data Sheet – Pages 2 and 3</title>
<link rel="stylesheet" href="https://fonts.googleapis.com/css2?family=Source+Sans+3:wght@400;600;700&display=swap">
<style>
  :root {
    --canvas: #ffffff;
    --page: #f3f4f5;
    --green: #63c07f;
    --tab: #3b3b3b;
    --ink: #444444;
    --white: #ffffff;
  }
  * { margin: 0; padding: 0; box-sizing: border-box; }
  html, body { width: 1200px; height: 1023px; overflow: hidden; background: var(--canvas); }
  body { position: relative; font-family: "Source Sans 3", Arial, sans-serif; color: var(--ink); }

  .page {
    position: absolute; top: 170px; height: 702px; width: 546px;
    background: var(--page);
    box-shadow: 0 6px 14px rgba(0,0,0,0.12);
  }
  .page--left { left: 41px; }
  .page--right { left: 611px; }

  .section-bar {
    position: absolute; height: 28px; background: var(--green);
    color: var(--white); font-weight: 700; font-size: 11px;
    line-height: 28px; letter-spacing: 0.1px;
  }
  .section-tab { position: absolute; width: 38px; height: 28px; background: var(--tab); }

  .page--left .section-bar { left: 0; width: 498px; padding-left: 42px; }
  .page--left .section-tab { left: 508px; }
  .page--right .section-bar { left: 0; width: 501px; padding-left: 44px; }
  .page--right .section-tab { left: 508px; }

  .body-text { position: absolute; font-size: 9.6px; line-height: 12.3px; text-align: justify; }
  .page--left .body-text { left: 42px; width: 340px; }

  .label { position: absolute; left: 42px; color: var(--green); font-size: 10px; font-weight: 600; }
  .aid-text { position: absolute; left: 55px; width: 328px; font-size: 9.6px; line-height: 12.3px; text-align: justify; }

  .fire-list {
    position: absolute; left: 50px; top: 514px; padding-left: 9px;
    border-left: 1px solid var(--ink);
    font-size: 9.6px; line-height: 12.3px; list-style: none;
  }

  .block { position: absolute; left: 44px; width: 457px; }
  .block h3 { color: var(--green); font-size: 11.5px; font-weight: 600; margin-bottom: 4px; line-height: 13px; }
  .block p { font-size: 9.4px; line-height: 12.3px; text-align: justify; }
</style>
</head>
<body>

<section class="page page--left">
  <div class="section-bar" style="top:52px">Section 2 - Hazards Identification</div>
  <div class="section-tab" style="top:52px"></div>
  <p class="body-text" style="top:95px">Class of division is 9, This product is safe under normal use.Health Hazards (Acute and Chronic) These chemicals are contained in a sealed enclosure. Risk of exposure occurs only if the battery is mechanically, thermally or electrically abused to the point of compromisingthe enclosure. Contact of electrolyte and extruded lithium with skin and eyes should be avoided.Sign/Symptoms of ExposureA shorted lithium batter can cause thermal and chemical burns upon contact with the skin.</p>

  <div class="section-bar" style="top:196px">Section 3 - First Aid Measures</div>
  <div class="section-tab" style="top:196px"></div>

  <h4 class="label" style="top:237px">Eye Contact</h4>
  <p class="aid-text" style="top:252px">Flush eyes with plenty of water for at least 15 minutes, occasionally lif&nbsp; ting the upper and lower eyelids.<br>Get medical aid.</p>

  <h4 class="label" style="top:298px">Skin Contact</h4>
  <p class="aid-text" style="top:315px">Remove contaminated clothes and rinse skin with plenty of water or shower for 15 minutes.<br>Get medical aid.</p>

  <h4 class="label" style="top:361px">Inhalation</h4>
  <p class="aid-text" style="top:373px;left:56px">Remove from exposure and move to fresh air immediately. Use oxygen if available.</p>

  <h4 class="label" style="top:406px;left:43px">Ingestion</h4>
  <p class="aid-text" style="top:424px">Give atleast 2 glasses of milk or water. Induce vomitting unless patient is uncoinscious.<br>Call a physician.</p>

  <div class="section-bar" style="top:475px">Section&nbsp; 4 - Fire Fighting Measures</div>
  <div class="section-tab" style="top:475px"></div>

  <ul class="fire-list">
    <li>Flash Point: N/A.</li>
    <li>Auto-Ignition Temperature: N/A.</li>
    <li>Extinguishing Media</li>
    <li>Dry chemical, CO2.</li>
    <li>Special Fire-Fighting Procedures</li>
    <li>Self-contained breathing apparatus.</li>
    <li>Unusual Fire and Explosion Hazards</li>
    <li>Cell may vent when subjected to excessive heat-exposing battery contents.</li>
    <li>Hazardous Combustion Products</li>
    <li>Carbon monoxide, carbon dioxide, lithium oxide fumes.</li>
  </ul>
</section>

<section class="page page--right">
  <div class="section-bar" style="top:48px">Section 5 - Accidental Release Measures</div>
  <div class="section-tab" style="top:48px"></div>

  <div class="block" style="top:89px">
    <h3>Steps to be Taken in case Material is Released or Spilled</h3>
    <p style="margin-top:7px">If the battery material is released, remove personnel from area until fumes dissipate. Provide maximum ventilation to clear out hazardous gases. Wipe it up with a cloth, and dispose of it in a plastic bag and put into a steel can. The preferred response is to leave the area and allow the batteries to cool and vapors to dissipate. Provide maximum ventilation. Avoid skin and eye contact or inhalation of vapors.</p>
  </div>

  <div class="block" style="top:168px">
    <h3>Waste Disposal Method</h3>
    <p>It is recommended to discharge the battery to the end, handing in the abandoned batteries to related department unified, dispose of the batteries in accordance with approved local, state, and federal requirements. Consult state environmental protection agency and/or federal EPA.</p>
  </div>

  <div class="section-bar" style="top:243px">Section 6 - Handling And Storage</div>
  <div class="section-tab" style="top:243px"></div>

  <div class="block" style="top:288px">
    <p>The batteries should not be opened, destroyed or incinerate, since theymay leak or rupture and release to the environment the ingredients that they contain in the hermetically sealed container. Do not short circuit terminals, or over charge the battery, forced over-discharge, throw to fire. Do not crush or puncture the battery, or immerse in liquids.</p>
  </div>

  <div class="block" style="top:346px">
    <h3>Precautions to be taken in handling and storing</h3>
    <p>Avoid mechanical or electrical abuse. Stored preferably in cool, dry and well-ventilated area, which is subject to little temperature change. Storage at high temperatures should be avoided. Do not place the battery near heating equipment, nor expose to direct sunlight for long periods.</p>
  </div>

  <div class="block" style="top:409px">
    <h3>Other Precautions</h3>
    <p>Batteries may explode or cause burns, if disassembled, crushed or exposed to fire or high temperatures.<br>Do not short or install with incorrect polarity.</p>
  </div>

  <div class="section-bar" style="top:467px">Section 7 - Exposure Controls, Personal Protection</div>
  <div class="section-tab" style="top:467px"></div>

  <div class="block" style="top:509px">
    <h3>Respiratory Protection</h3>
    <p>In case of battery venting, provide as much ventilation as possible. Avoid confined areas with venting batteries. Respiratory protection is not necessary under conditions of normal use.</p>
  </div>

  <div class="block" style="top:559px">
    <h3>Ventilation</h3>
    <p>Not necessary under conditions of normal use.</p>
  </div>

  <div class="block" style="top:595px">
    <h3>Protective Gloves</h3>
    <p>Not necessary under conditions of normal use.</p>
  </div>

  <div class="block" style="top:631px">
    <h3>Other Protective Clothing or Equipment</h3>
    <p style="text-align:left">Not necessary under conditions of normal use. Personal Protection is recommended for venting batteries: Respiratory protection, protective gloves, protective clothing and safety glass with side shields.</p>
  </div>
</section>

</body>
</html>
```